Pulsewell Power sharing solutions, we offer different types of mobile charging stations for all ty

I need an app that shows all the locations that use our charging stations.
the app should show the following:

1. a map where client can see where all the stations are
2. a map that shows which one is the nearest charging station based on the persons location
3. a search tab where you can pick the city ( all will be based from sweden) and we will start with two cities: Gothenburg and Stockholm. So user will be able to pick the city and than get a list of all venues using our stations. along the way we will keep adding cities and countries but for now i need a design, something i can show potential customers on a power point how this app will work.
4. a list of different venue categories:
- restaurant
- café
- Festival
- Airport
- Library
- Night club
- Shopping center

Once client chooses the city, they can also choose what they are looking for and choose for example which restaurant to eat at based on if they have our charging station or not

you can of course improvise on ideas, if you come up with something and want to add to the app design thats ok, I'm up for suggestions.

in conclusion: the purpose for the app is for users to be able to search for charging stations or see where the nearest charging station is

Target Market(s)

Everyone

Requirements
Must have
• professional and simple design

```html
<!DOCTYPE html>
<html lang="en">
<head>
<meta charset="utf-8">
<title>Pulsewell Power – App Screens</title>
<link rel="stylesheet" href="https://fonts.googleapis.com/css2?family=Montserrat:wght@400;500;600&display=swap">
<style>
  :root{
    --page:#f6f6f6;
    --white:#ffffff;
    --green:#3db54a;
    --ink:#333333;
    --muted:#8a8a8a;
    --line:#e6e6e6;
    --blue:#3fa4f3;
    --pink:#ee4f86;
    --tan:#d8b06a;
    --soft:#ececec;
    --map-a:#f4ecd6;
    --map-b:#e9e4d8;
    --radius-blue:rgba(96,160,230,.28);
  }
  *{box-sizing:border-box;margin:0;padding:0}
  html,body{width:960px;height:1200px;overflow:hidden}
  body{background:var(--page);font-family:"Montserrat",sans-serif;color:var(--ink);position:relative}
  .defs{position:absolute;width:0;height:0}

  .screen{position:absolute;width:233px;height:415px;background:var(--white);overflow:hidden;border:1px solid #d4d4d4}
  .col-1{left:79px}.col-2{left:358px}.col-3{left:638px}
  .row-1{top:105px}.row-2{top:690px}
  .screen--green{background:var(--green);border-color:var(--green)}

  .status-bar{position:absolute;top:0;left:0;right:0;height:14px;display:flex;align-items:center;justify-content:space-between;padding:0 5px;font-size:6.5px;font-weight:500;color:#111;z-index:6}
  .screen--green .status-bar{color:#fff}
  .status-bar .carrier{display:flex;align-items:center;gap:2px}
  .signal{display:inline-flex;align-items:flex-end;gap:1px;height:6px}
  .signal i{display:block;width:1.4px;background:currentColor}
  .signal i:nth-child(1){height:2px}.signal i:nth-child(2){height:3.5px}.signal i:nth-child(3){height:5px}.signal i:nth-child(4){height:6px}
  .battery{display:inline-flex;align-items:center;gap:3px}
  .battery b{display:inline-block;width:12px;height:6px;border:1px solid currentColor;border-radius:1px;position:relative}
  .battery b::after{content:"";position:absolute;left:1px;top:1px;bottom:1px;width:5px;background:currentColor}

  /* Splash */
  .splash{position:absolute;inset:0;display:flex;flex-direction:column;align-items:center}
  .splash .mark{width:88px;height:88px;border-radius:50%;margin-top:110px;background:var(--green)}
  .splash--soft .mark{background:#f1f1f1}
  .screen--green .mark{background:var(--white)}
  .brand-name{margin-top:18px;font-size:19px;font-weight:500;letter-spacing:.2px;color:var(--ink)}
  .tagline{margin-top:6px;font-size:8.5px;letter-spacing:3px;font-weight:500;color:var(--ink)}
  .screen--green .brand-name,.screen--green .tagline{color:var(--white)}

  /* Map */
  .map{position:absolute;inset:0;background:linear-gradient(160deg,#dfe8cf 0%,var(--map-a) 25%,var(--map-b) 60%,var(--map-a) 100%)}
  .map-overlay{position:absolute;inset:0}
  .map-dim{position:absolute;inset:0;background:rgba(20,20,20,.42);z-index:3}
  .pin-label{font-size:6.3px;font-weight:600}
  .pin-label--food{fill:#3a8fd9}.pin-label--shop{fill:#e84c84}.pin-label--cafe{fill:#c99a45}

  .top-card{position:absolute;left:6px;top:24px;width:221px;height:35px;background:var(--white);border-radius:4px;box-shadow:0 2px 6px rgba(0,0,0,.15);z-index:5}
  .top-card .menu{position:absolute;left:12px;top:13px;width:13px}
  .top-card .menu i{display:block;height:1.6px;background:var(--green);margin-bottom:2.4px}
  .top-card .menu i:nth-child(2){width:9px}
  .top-card .city{position:absolute;left:0;right:0;top:12px;text-align:center;font-size:9px;letter-spacing:.8px;font-weight:500}
  .top-card .search{position:absolute;right:10px;top:9px}
  .top-card .chev{position:absolute;left:50%;bottom:3px;transform:translateX(-50%)}

  .filters{position:absolute;left:6px;top:24px;width:221px;height:227px;background:var(--white);border-radius:4px;z-index:5;overflow:hidden}
  .filters .header{position:relative;height:35px}
  .filters-title{height:20px;background:#f4f4f4;font-size:7.5px;color:var(--muted);text-align:center;line-height:20px}
  .filter-grid{display:grid;grid-template-columns:repeat(4,1fr);padding:12px 4px 0;row-gap:20px}
  .filter{display:flex;flex-direction:column;align-items:center;text-align:center}
  .filter span{margin-top:3px;font-size:7px;line-height:1.2;color:#555;min-height:17px}
  .filters .collapse{position:absolute;left:50%;bottom:8px;transform:translateX(-50%)}

  .nearby-btn{position:absolute;left:80px;top:374px;width:72px;height:72px;border-radius:50%;background:var(--white);box-shadow:0 0 8px rgba(0,0,0,.18);text-align:center;z-index:5}
  .nearby-btn--active{border:2px solid var(--green)}
  .nearby-btn svg{margin-top:10px}
  .nearby-btn span{display:block;font-size:9px;color:#555;margin-top:2px}

  .places{position:absolute;left:6px;top:200px;width:221px;height:204px;background:var(--white);border-radius:4px;box-shadow:0 -2px 8px rgba(0,0,0,.12);z-index:5;overflow:hidden}
  .places h2{font-size:9px;font-weight:500;text-align:center;margin-top:12px}
  .places .chev{display:block;margin:2px auto 0}
  .place{position:absolute;top:38px;width:90px;text-align:center}
  .place .name{font-size:8.5px;font-weight:500;margin-top:6px}
  .place .dist{font-size:7.5px;color:var(--muted);margin-top:5px}
  .place .go{margin-top:7px}
</style>
</head>
<body>

<svg class="defs" aria-hidden="true">
  <defs>
    <symbol id="pick" viewBox="0 0 40 40"><path d="M20 2C31 2 38 5 38 13C38 24 27 38 20 38C13 38 2 24 2 13C2 5 9 2 20 2Z"/></symbol>
    <symbol id="pin-food" viewBox="0 0 20 22"><path d="M10 1C16 1 19 3 19 7.5C19 13 13.5 21 10 21C6.5 21 1 13 1 7.5C1 3 4 1 10 1Z" fill="#3fa4f3" stroke="#fff" stroke-width="1.4"/><path d="M6.5 5.5L13.5 12.5M13.5 5.5L6.5 12.5" stroke="#fff" stroke-width="1.7" stroke-linecap="round"/></symbol>
    <symbol id="pin-shop" viewBox="0 0 20 22"><path d="M10 1C16 1 19 3 19 7.5C19 13 13.5 21 10 21C6.5 21 1 13 1 7.5C1 3 4 1 10 1Z" fill="#ee4f86" stroke="#fff" stroke-width="1.4"/><rect x="6.3" y="7" width="7.4" height="6.4" rx=".6" fill="none" stroke="#fff" stroke-width="1.3"/><path d="M8.2 7V5.8a1.8 1.8 0 0 1 3.6 0V7" fill="none" stroke="#fff" stroke-width="1.2"/></symbol>
    <symbol id="pin-cafe" viewBox="0 0 20 22"><path d="M10 1C16 1 19 3 19 7.5C19 13 13.5 21 10 21C6.5 21 1 13 1 7.5C1 3 4 1 10 1Z" fill="#d8b06a" stroke="#fff" stroke-width="1.4"/><path d="M6.5 5.5L13.5 12.5M13.5 5.5L6.5 12.5" stroke="#fff" stroke-width="1.7" stroke-linecap="round"/></symbol>
    <symbol id="chev-down" viewBox="0 0 12 6"><path d="M2 1.5L6 4.5L10 1.5" fill="none" stroke="#3db54a" stroke-width="1.8" stroke-linecap="round"/></symbol>
    <symbol id="chev-up" viewBox="0 0 12 6"><path d="M2 4.5L6 1.5L10 4.5" fill="none" stroke="#3db54a" stroke-width="1.8" stroke-linecap="round"/></symbol>
  </defs>
</svg>

<!-- Splash, white -->
<section class="screen col-1 row-1">
  <div class="status-bar"><span class="carrier"><span class="signal"><i></i><i></i><i></i><i></i></span> Telora</span><span>9:41 AM</span><span class="battery">58 % <b></b></span></div>
  <div class="splash">
    <div class="mark"></div>
    <p class="brand-name">Pulsewell Power</p>
    <p class="tagline">Charging solutions</p>
  </div>
</section>

<!-- Splash, soft -->
<section class="screen col-2 row-1">
  <div class="status-bar"><span class="carrier"><span class="signal"><i></i><i></i><i></i><i></i></span> Telora</span><span>9:41 AM</span><span class="battery">58 % <b></b></span></div>
  <div class="splash splash--soft">
    <div class="mark"></div>
    <p class="brand-name">Pulsewell Power</p>
    <p class="tagline">Charging solutions</p>
  </div>
</section>

<!-- Splash, green -->
<section class="screen screen--green col-3 row-1">
  <div class="status-bar"><span class="carrier"><span class="signal"><i></i><i></i><i></i><i></i></span> Telora</span><span>9:41 AM</span><span class="battery">58 % <b></b></span></div>
  <div class="splash">
    <div class="mark"></div>
    <p class="brand-name">Pulsewell Power</p>
    <p class="tagline">Charging solutions</p>
  </div>
</section>

<!-- Map -->
<section class="screen col-1 row-2">
  <div class="map" role="img" aria-label="Street map of central Stockholm"></div>
  <svg class="map-overlay" width="233" height="415" viewBox="0 0 233 415">
    <circle cx="118" cy="188" r="50" fill="var(--radius-blue)" stroke="rgba(96,160,230,.5)"/>
    <use href="#pin-food" x="179" y="60" width="20" height="22"/>
    <use href="#pin-food" x="36" y="115" width="20" height="22"/>
    <use href="#pin-food" x="174" y="185" width="20" height="22"/>
    <use href="#pin-food" x="18" y="201" width="20" height="22"/>
    <use href="#pin-food" x="211" y="247" width="20" height="22"/>
    <use href="#pin-shop" x="130" y="188" width="20" height="22"/>
    <use href="#pin-shop" x="5" y="283" width="20" height="22"/>
    <use href="#pin-shop" x="66" y="295" width="20" height="22"/>
    <use href="#pin-shop" x="178" y="275" width="20" height="22"/>
    <use href="#pin-cafe" x="152" y="375" width="20" height="22"/>
    <circle cx="118" cy="188" r="10" fill="#c98e6e" stroke="#fff" stroke-width="2" role="img" aria-label="User profile photo"/>
    <text class="pin-label pin-label--food" x="14" y="109">Fresh Deli Norra</text>
    <text class="pin-label pin-label--shop" x="133" y="182">Bella Mode</text>
    <text class="pin-label pin-label--food" x="180" y="179">Hall 9</text>
    <text class="pin-label pin-label--food" x="10" y="194">Torghallen</text>
    <text class="pin-label pin-label--food" x="195" y="242">Tapas Casa</text>
    <text class="pin-label pin-label--shop" x="7" y="277">VESTA</text>
    <text class="pin-label pin-label--shop" x="55" y="289">Nils Berg</text>
    <text class="pin-label pin-label--shop" x="163" y="269">City Threads</text>
    <text class="pin-label pin-label--cafe" x="142" y="368">Cafe Lumo</text>
  </svg>
  <div class="status-bar"><span class="carrier"><span class="signal"><i></i><i></i><i></i><i></i></span> Telora</span><span>9:41 AM</span><span class="battery">58 % <b></b></span></div>
  <header class="top-card">
    <span class="menu"><i></i><i></i><i></i></span>
    <p class="city">STOCKHOLM</p>
    <svg class="search" width="17" height="17" viewBox="0 0 17 17"><circle cx="7" cy="7" r="5.6" fill="none" stroke="#3db54a" stroke-width="1.4"/><path d="M11 11L15.5 15.5" stroke="#3db54a" stroke-width="1.4" stroke-linecap="round"/></svg>
    <svg class="chev" width="12" height="6"><use href="#chev-down"/></svg>
  </header>
  <div class="nearby-btn"><svg width="12" height="6"><use href="#chev-up"/></svg><span>Nearby</span></div>
</section>

<!-- Filters -->
<section class="screen col-2 row-2">
  <div class="map" role="img" aria-label="Street map of central Stockholm"></div>
  <svg class="map-overlay" width="233" height="415" viewBox="0 0 233 415">
    <use href="#pin-food" x="211" y="247" width="20" height="22"/>
    <use href="#pin-shop" x="5" y="283" width="20" height="22"/>
    <use href="#pin-shop" x="66" y="295" width="20" height="22"/>
    <use href="#pin-shop" x="178" y="275" width="20" height="22"/>
    <use href="#pin-cafe" x="152" y="375" width="20" height="22"/>
    <text class="pin-label pin-label--shop" x="7" y="277">VESTA</text>
    <text class="pin-label pin-label--shop" x="55" y="289">Nils Berg</text>
    <text class="pin-label pin-label--shop" x="163" y="269">City Threads</text>
    <text class="pin-label pin-label--cafe" x="142" y="368">Cafe Lumo</text>
  </svg>
  <div class="map-dim"></div>
  <div class="status-bar"><span class="carrier"><span class="signal"><i></i><i></i><i></i><i></i></span> Telora</span><span>9:41 AM</span><span class="battery">58 % <b></b></span></div>
  <div class="filters">
    <header class="header">
      <div class="top-card" style="left:0;top:0;box-shadow:none">
        <span class="menu"><i></i><i></i><i></i></span>
        <p class="city">STOCKHOLM</p>
        <svg class="search" width="17" height="17" viewBox="0 0 17 17"><circle cx="7" cy="7" r="5.6" fill="none" stroke="#3db54a" stroke-width="1.4"/><path d="M11 11L15.5 15.5" stroke="#3db54a" stroke-width="1.4" stroke-linecap="round"/></svg>
      </div>
    </header>
    <p class="filters-title">Filters</p>
    <div class="filter-grid">
      <div class="filter">
        <svg width="30" height="30" viewBox="0 0 40 40"><use href="#pick" fill="var(--blue)"/><path d="M14 13L26 25M26 13L14 25" stroke="#fff" stroke-width="2.4" stroke-linecap="round"/></svg>
        <span>Restaurant</span>
      </div>
      <div class="filter">
        <svg width="30" height="30" viewBox="0 0 40 40"><use href="#pick" fill="var(--pink)"/><rect x="14" y="15" width="12" height="10" rx="1" fill="none" stroke="#fff" stroke-width="2"/><path d="M17 15V13a3 3 0 0 1 6 0V15" fill="none" stroke="#fff" stroke-width="1.8"/></svg>
        <span>Shopping Center</span>
      </div>
      <div class="filter">
        <svg width="30" height="30" viewBox="0 0 40 40"><use href="#pick" fill="var(--tan)"/><path d="M13 14H25V19a5 5 0 0 1-5 5h-2a5 5 0 0 1-5-5Z" fill="#fff"/><path d="M25 15.5h2a2 2 0 0 1 0 4h-2" fill="none" stroke="#fff" stroke-width="1.6"/><path d="M12 26H26" stroke="#fff" stroke-width="1.6"/></svg>
        <span>Cafe</span>
      </div>
      <div class="filter">
        <svg width="30" height="30" viewBox="0 0 40 40"><use href="#pick" fill="var(--soft)"/><path d="M20 10L27 26H13Z" fill="#555"/><path d="M20 18L23 26H17Z" fill="#ececec"/></svg>
        <span>Festival</span>
      </div>
      <div class="filter">
        <svg width="30" height="30" viewBox="0 0 40 40"><use href="#pick" fill="var(--soft)"/><path d="M12 22L28 14M17 19.5L14 14.5M22 17L21 25.5" stroke="#555" stroke-width="2.2" stroke-linecap="round"/></svg>
        <span>Airport</span>
      </div>
      <div class="filter">
        <svg width="30" height="30" viewBox="0 0 40 40"><use href="#pick" fill="var(--soft)"/><path d="M12 13h6.5a1.5 1.5 0 0 1 1.5 1.5V26c0-1-1-1.5-2-1.5H12ZM28 13h-6.5A1.5 1.5 0 0 0 20 14.5V26c0-1 1-1.5 2-1.5H28Z" fill="#555"/></svg>
        <span>Library</span>
      </div>
      <div class="filter">
        <svg width="30" height="30" viewBox="0 0 40 40"><use href="#pick" fill="var(--soft)"/><path d="M13 12H27L20 20Z" fill="#555"/><path d="M20 20V27M16 27H24" stroke="#555" stroke-width="1.8" stroke-linecap="round"/></svg>
        <span>Night Club</span>
      </div>
    </div>
    <svg class="collapse" width="12" height="6"><use href="#chev-up"/></svg>
  </div>
  <div class="nearby-btn nearby-btn--active"><svg width="12" height="6"><use href="#chev-up"/></svg><span>Nearby</span></div>
</section>

<!-- Places nearby -->
<section class="screen col-3 row-2">
  <div class="map" role="img" aria-label="Street map of central Stockholm"></div>
  <svg class="map-overlay" width="233" height="415" viewBox="0 0 233 415">
    <circle cx="118" cy="188" r="50" fill="var(--radius-blue)" stroke="rgba(96,160,230,.5)"/>
    <use href="#pin-food" x="179" y="60" width="20" height="22"/>
    <use href="#pin-food" x="36" y="115" width="20" height="22"/>
    <use href="#pin-food" x="174" y="185" width="20" height="22"/>
    <use href="#pin-food" x="18" y="201" width="20" height="22"/>
    <use href="#pin-shop" x="130" y="188" width="20" height="22"/>
    <circle cx="118" cy="188" r="10" fill="#c98e6e" stroke="#fff" stroke-width="2" role="img" aria-label="User profile photo"/>
    <text class="pin-label pin-label--food" x="14" y="109">Fresh Deli Norra</text>
    <text class="pin-label pin-label--shop" x="133" y="182">Bella Mode</text>
    <text class="pin-label pin-label--food" x="180" y="179">Hall 9</text>
    <text class="pin-label pin-label--food" x="10" y="194">Torghallen</text>
  </svg>
  <div class="status-bar"><span class="carrier"><span class="signal"><i></i><i></i><i></i><i></i></span> Telora</span><span>9:41 AM</span><span class="battery">58 % <b></b></span></div>
  <header class="top-card">
    <span class="menu"><i></i><i></i><i></i></span>
    <p class="city">STOCKHOLM</p>
    <svg class="search" width="17" height="17" viewBox="0 0 17 17"><circle cx="7" cy="7" r="5.6" fill="none" stroke="#3db54a" stroke-width="1.4"/><path d="M11 11L15.5 15.5" stroke="#3db54a" stroke-width="1.4" stroke-linecap="round"/></svg>
    <svg class="chev" width="12" height="6"><use href="#chev-down"/></svg>
  </header>
  <div class="places">
    <h2>Places Nearby</h2>
    <svg class="chev" width="12" height="6"><use href="#chev-down"/></svg>

    <div class="place" style="left:3px">
      <svg width="76" height="76" viewBox="0 0 40 40" role="img" aria-label="Photo of the Bella Mode shop front"><defs><linearGradient id="g1" x1="0" y1="0" x2="0" y2="1"><stop offset="0" stop-color="#6b5544"/><stop offset="1" stop-color="#2b2420"/></linearGradient></defs><use href="#pick" fill="url(#g1)"/></svg>
      <p class="name">Bella Mode</p>
      <p class="dist">10 Meters</p>
      <svg class="go" width="26" height="26" viewBox="0 0 40 40"><use href="#pick" fill="var(--green)"/><path d="M15 28V19h9" fill="none" stroke="#fff" stroke-width="3"/><path d="M22 14l6 5-6 5Z" fill="#fff"/></svg>
    </div>

    <div class="place" style="left:94px">
      <svg width="76" height="76" viewBox="0 0 40 40" role="img" aria-label="Photo of the Hall 9 restaurant at night"><defs><linearGradient id="g2" x1="0" y1="0" x2="0" y2="1"><stop offset="0" stop-color="#4a4a4a"/><stop offset="1" stop-color="#1c1c1c"/></linearGradient></defs><use href="#pick" fill="url(#g2)"/></svg>
      <p class="name">Hall 9</p>
      <p class="dist">15 Meters</p>
      <svg class="go" width="26" height="26" viewBox="0 0 40 40"><use href="#pick" fill="var(--green)"/><path d="M15 28V19h9" fill="none" stroke="#fff" stroke-width="3"/><path d="M22 14l6 5-6 5Z" fill="#fff"/></svg>
    </div>

    <div class="place" style="left:185px">
      <svg width="76" height="76" viewBox="0 0 40 40" role="img" aria-label="Photo of the Torghallen food hall"><defs><linearGradient id="g3" x1="0" y1="0" x2="0" y2="1"><stop offset="0" stop-color="#7a6a55"/><stop offset="1" stop-color="#3a322a"/></linearGradient></defs><use href="#pick" fill="url(#g3)"/></svg>
      <p class="name">Torghallen</p>
      <p class="dist">20 Meters</p>
      <svg class="go" width="26" height="26" viewBox="0 0 40 40"><use href="#pick" fill="var(--green)"/><path d="M15 28V19h9" fill="none" stroke="#fff" stroke-width="3"/><path d="M22 14l6 5-6 5Z" fill="#fff"/></svg>
    </div>
  </div>
</section>

</body>
</html>
```